Real Estate Investing company needs a business card design

We need a business card design for new Real Estate Investment Company called "Maple Ridge Ventures, LLC." We buy homes for cash and close quickly in any situation. Our company provides an easy and fast option for home owners who are in tough situations who need to sell their home fast and don't want realtor fees or other listing hassles. We also renovate and resell our homes which helps provide housing for the community. We would like to see designs that use the colors blue and white to match our company logo or other colors that may match our company logo. The final design should communicate trust and easy process.
Industry/Entity Type
Business
Contact Information for Business Card
Front should have company name and company logo. back of card should have company logo and area to list services.
Look and feel

```html
<!DOCTYPE html>
<html lang="en">
<head>
<meta charset="utf-8">
<title>Maple Ridge Ventures – Business Card</title>
<link rel="stylesheet" href="https://fonts.googleapis.com/css2?family=Open+Sans:wght@400;600;700&display=swap">
<style>
  :root {
    --brand-blue: #1f74bf;
    --brand-blue-light: #2b8ad6;
    --ink-gray: #7a7f85;
    --paper: #ffffff;
    --backdrop: #e7e4df;
  }
  * { margin: 0; padding: 0; box-sizing: border-box; }
  html, body { width: 1200px; height: 1023px; overflow: hidden; }
  body {
    background: var(--backdrop);
    font-family: "Open Sans", Arial, sans-serif;
    position: relative;
  }
  .card {
    position: absolute;
    width: 680px;
    height: 389px;
    border-radius: 4px;
    box-shadow: 0 6px 18px rgba(0,0,0,0.18);
    overflow: hidden;
  }
  /* Front */
  .card-front { left: 90px; top: 80px; background: var(--paper); }
  .divider-rule {
    position: absolute; left: 44px; right: 34px; top: 262px;
    height: 2px; background: var(--brand-blue);
  }
  .front-wordmark {
    position: absolute; left: 44px; top: 58px;
    color: var(--brand-blue);
    font-weight: 700; font-size: 48px; line-height: 1.05;
    letter-spacing: 1px;
  }
  .holder {
    position: absolute; left: 44px; top: 214px;
    font-size: 17px; color: var(--ink-gray);
  }
  .holder-name { color: var(--brand-blue); font-weight: 700; letter-spacing: 1px; }
  .holder-divider { margin: 0 8px; color: var(--brand-blue); }
  .contact-list {
    position: absolute; left: 44px; top: 286px;
    list-style: none; font-size: 15px; color: var(--ink-gray);
  }
  .contact-list li { display: flex; align-items: center; gap: 10px; height: 26px; }
  .contact-icon { width: 14px; height: 14px; flex: none; }
  .company-address {
    position: absolute; right: 34px; top: 290px;
    text-align: right; font-size: 15px; line-height: 1.45; color: var(--ink-gray);
    font-style: normal;
  }
  .company-name { color: var(--brand-blue); font-weight: 700; }

  /* Back */
  .card-back {
    left: 430px; top: 560px;
    background: linear-gradient(135deg, var(--brand-blue-light), var(--brand-blue));
    color: var(--paper);
    text-align: center;
    display: flex; flex-direction: column; align-items: center; justify-content: center;
  }
  .back-wordmark {
    font-weight: 700; font-size: 44px; line-height: 1.05; letter-spacing: 1px;
  }
  .services {
    margin-top: 30px; width: 600px;
    font-size: 14.5px; line-height: 1.55;
  }
</style>
</head>
<body>
  <section class="card card-front" aria-label="Business card front">
    <div class="front-wordmark">MAPLE RIDGE<br>VENTURES</div>
    <p class="holder"><span class="holder-name">DMORGAN</span><span class="holder-divider">|</span>Director</p>
    <div class="divider-rule" aria-hidden="true"></div>
    <ul class="contact-list">
      <li>
        <svg class="contact-icon" viewBox="0 0 14 14" aria-hidden="true"><rect width="14" height="14" rx="2" fill="var(--brand-blue)"/><path d="M4 3.5 L5.8 3.5 L6.3 5.6 L5.3 6.3 Q6.2 8 7.7 8.7 L8.4 7.7 L10.5 8.2 L10.5 10 Q6.5 10.5 4 6 Z" fill="#fff"/></svg>
        555.214.0187
      </li>
      <li>
        <svg class="contact-icon" viewBox="0 0 14 14" aria-hidden="true"><rect width="14" height="14" rx="2" fill="var(--brand-blue)"/><rect x="3" y="4.5" width="8" height="5.5" fill="none" stroke="#fff" stroke-width="1"/><path d="M3 4.5 L7 7.8 L11 4.5" fill="none" stroke="#fff" stroke-width="1"/></svg>
        dmorgan@mapleridgeventures.com
      </li>
      <li>
        <svg class="contact-icon" viewBox="0 0 14 14" aria-hidden="true"><rect width="14" height="14" rx="2" fill="var(--brand-blue)"/><circle cx="7" cy="7" r="3.8" fill="none" stroke="#fff" stroke-width="1"/><path d="M3.2 7 H10.8 M7 3.2 V10.8" stroke="#fff" stroke-width="0.8"/></svg>
        www.mapleridgeventures.com
      </li>
    </ul>
    <address class="company-address">
      <span class="company-name">Maple Ridge Ventures, LLC.</span><br>
      118 Birchwood Lane,<br>
      Fairview, TX 75069
    </address>
  </section>

  <section class="card card-back" aria-label="Business card back">
    <div class="back-wordmark">MAPLE RIDGE<br>VENTURES</div>
    <p class="services">
      We buy homes for cash and close quickly in any situation.
      Our company provides an easy and fast option for home owners
      who are in tough situations who need to sell their home fast and
      don't want realtor fees or other listing hassles.
      We also renovate and resell our homes which helps provide
      housing for the community.
    </p>
  </section>
</body>
</html>
```